Bold Website Design for Fitness Trainer - No Coding

We are in need of a bold and unique website design for a personal fitness training company, www.TessaLorvel.com. We need DESIGN ONLY for three pages. These will be a homepage, a lead capture page, and one internal page with a sidebar. The design will be used for coding a wordpress theme, if that matters for the designer.

Tessa Lorvel Fitness Training
2738 E 19th St #415
Austin, TX 78705
512-607-4918
http://www.tessalorvel.com

Target Market(s)

18-45 year old male and females making 80k+ a year and looking to get stronger and in shape.

Industry/Entity Type

Fitness

Number of Pages Required

3 page

Font styles to use
Sans Serif

Requirements
Must have
• See attached design specs file.
Nice to have
Should not have
• Boxed layout.
• Dark Background.

```html
<!DOCTYPE html>
<html lang="en">
<head>
<meta charset="utf-8">
<title>Tessa Lorvel Fitness Training – Homepage</title>
<link href="https://fonts.googleapis.com/css2?family=Cardo:wght@400;700&family=Arimo:wght@400;700&display=swap" rel="stylesheet">
<style>
:root{
  --stage:#e9e7e4;
  --white:#ffffff;
  --ink:#222222;
  --muted:#666666;
  --dark:#1b1b1b;
  --footer:#262626;
  --hero-a:#2a2a2a;
  --hero-b:#6b6b6b;
  --pink:#e5357c;
  --cyan:#27b6d9;
  --yellow:#f2c230;
  --blue:#2f6db3;
  --line:#d6d6d6;
}
*{box-sizing:border-box;margin:0;padding:0}
html,body{width:1200px;height:848px;overflow:hidden;background:var(--stage)}
body{font-family:"Arimo",Arial,sans-serif;color:var(--ink);position:relative}
.page{position:absolute;left:416px;top:12px;width:368px;height:788px;background:var(--white);
  transform:scale(1.05);transform-origin:top center;box-shadow:0 4px 18px rgba(0,0,0,.25);overflow:hidden}
.abs{position:absolute}
.serif{font-family:"Cardo",Georgia,serif}

/* header */
.accent-strip{left:0;top:0;width:100%;height:2px;display:flex}
.accent-strip span{flex:1}
.header{left:0;top:2px;width:100%;height:46px}
.call{left:20px;top:16px;font-size:8px}
.call small{display:block;font-size:4px;color:var(--muted);margin-top:1px}
.brand{left:132px;top:11px;display:flex;align-items:center;gap:4px}
.brand-dot{width:22px;height:22px;border-radius:50%;background:var(--yellow)}
.brand-name{font-size:11px;font-weight:700;color:var(--ink)}
.share{right:14px;top:17px;display:flex;align-items:center;gap:2px;font-size:4px;color:var(--muted)}
.share i{width:7px;height:7px;border-radius:50%;background:#777;display:inline-block}

/* hero */
.hero{left:0;top:48px;width:100%;height:214px;background:linear-gradient(110deg,var(--hero-a),var(--hero-b) 55%,#3a3a3a)}
.nav{left:40px;top:8px;height:14px;display:flex;background:var(--white);font-size:4.6px}
.nav a{padding:0 5px;line-height:14px;color:var(--ink);text-decoration:none;border-right:1px solid var(--line)}
.nav a.active{background:#3a3a3a;color:var(--white)}
.nav .search{width:80px;margin-left:4px;color:#999;padding-left:22px;line-height:14px}
.dropdown{left:66px;top:22px;width:50px;background:var(--white);font-size:4.2px}
.dropdown li{list-style:none;padding:0 6px;line-height:16px;border-bottom:1px solid #eee}
.dropdown li.current{background:#d9d9d9}
.dots{left:7px;top:108px;display:flex;flex-direction:column;gap:4px}
.dots i{width:4px;height:4px;border-radius:50%;background:#999;display:block}
.dots i.on{background:var(--pink)}
.hero-title{right:15px;top:150px;font-size:15px;line-height:18px;color:var(--white);white-space:nowrap}
.hero-copy{right:15px;top:172px;width:205px;text-align:right;font-size:5.6px;line-height:7px;color:#eee}
.notch{width:34px;height:34px;border-radius:50%;left:167px}

/* programs */
.programs{left:0;top:262px;width:100%;height:190px}
.sec-title{width:100%;text-align:center;font-size:13px}
.sec-sub{width:100%;text-align:center;font-size:5px;color:var(--muted)}
.card{width:105px;top:44px}
.card .ph{height:76px}
.card h3{font-family:"Cardo",Georgia,serif;font-weight:400;font-size:7.5px;text-align:center;margin-top:8px}
.card p{font-size:4.4px;line-height:5.6px;text-align:center;color:var(--muted);margin-top:4px}
.card .more{display:block;text-align:center;color:var(--pink);font-size:4.4px;margin-top:3px}
.ph-label{display:flex;align-items:center;justify-content:center;color:#fff;font-size:6px}

/* join */
.join{left:0;top:452px;width:100%;height:108px;background:linear-gradient(90deg,#151515 40%,#5a5a5a)}
.join h2{left:18px;top:18px;font-size:14px;font-weight:400;color:var(--white)}
.join p{left:18px;top:38px;width:200px;font-size:5.2px;line-height:6.6px;color:#ddd}
.btn{left:18px;top:80px;width:62px;height:16px;background:var(--blue);color:var(--white);font-family:"Cardo",Georgia,serif;
  font-size:5.6px;line-height:16px;text-align:center;border-radius:2px}

/* success */
.success{left:0;top:560px;width:100%;height:142px}
.person{width:80px;top:32px;text-align:center}
.avatar{width:46px;height:46px;border-radius:50%;margin:0 auto;border:3px solid #eee;box-shadow:0 0 0 1px #ddd}
.person h4{font-family:"Cardo",Georgia,serif;font-weight:400;font-size:7px;margin-top:6px}
.person .role{font-size:3.8px;color:var(--muted)}
.person q{display:block;font-family:"Cardo",Georgia,serif;font-style:italic;font-size:4.4px;line-height:5.4px;margin-top:5px;quotes:none}

/* footer */
.footer{left:0;top:702px;width:100%;height:68px;background:var(--footer);color:#aaa;font-size:4px}
.f-head{font-family:"Cardo",Georgia,serif;font-size:5.4px;color:#bbb;white-space:nowrap}
.f-row{display:flex;align-items:center;gap:4px;margin-top:5px}
.f-row i{width:5px;height:5px;border-radius:50%;border:1px solid #888;display:inline-block}
.f-divider{left:94px;top:8px;width:1px;height:52px;background:#444}
.map{left:106px;top:18px;width:66px;height:25px;background:linear-gradient(135deg,#dedede,#c9c9c9)}
.social{right:10px;top:20px;display:flex;gap:3px}
.social i{width:8px;height:8px;border-radius:50%;background:#777;display:block}
.legal{right:10px;top:58px;font-size:3.8px}
.bottom{left:0;top:770px;width:100%;height:18px;background:#161616;color:#888;font-size:3.8px;text-align:center;line-height:18px}
</style>
</head>
<body>
<div class="page">
  <div class="abs accent-strip"><span style="background:var(--pink)"></span><span style="background:var(--cyan)"></span><span style="background:var(--yellow)"></span><span style="background:var(--pink)"></span></div>

  <header class="abs header">
    <svg class="abs" style="left:8px;top:16px" width="9" height="9" viewBox="0 0 24 24"><path fill="#222" d="M6.6 10.8a15 15 0 0 0 6.6 6.6l2.2-2.2c.3-.3.7-.4 1-.2 1.1.4 2.3.6 3.6.6.6 0 1 .4 1 1V20c0 .6-.4 1-1 1A17 17 0 0 1 3 4c0-.6.4-1 1-1h3.5c.6 0 1 .4 1 1 0 1.3.2 2.5.6 3.6.1.3 0 .7-.2 1z"/></svg>
    <div class="abs call">Call Me +1 888 204 671<small>on Business day 09:00 am - 06:00pm</small></div>
    <div class="abs brand"><span class="brand-dot"></span><span class="brand-name">Tessa Lorvel</span></div>
    <div class="abs share">Share With <i></i><i></i><i></i><i></i><i></i><i></i></div>
  </header>

  <section class="abs hero" role="img" aria-label="Athletes training in a gym, black and white photo">
    <nav class="abs nav">
      <a>Home</a><a class="active">Programs</a><a>Meet Your Trainer</a><a>Blog</a><a>Contact Me</a><a>Free Session</a>
      <span class="search">Quick Search ...</span>
    </nav>
    <ul class="abs dropdown">
      <li>Crossfit</li><li>Endurance</li><li class="current">Personal Training</li><li>Yoga / Mobility</li><li>Open Gym</li><li>Nutrition</li>
    </ul>
    <div class="abs dots"><i></i><i class="on"></i><i></i><i></i><i></i><i></i></div>
    <h1 class="abs hero-title serif" style="font-weight:400">Workouts custom tailored to you</h1>
    <p class="abs hero-copy">Our programs is designed for universal scalability making it the perfect application for any committed individual regardless of your experience, age, or fitness level</p>
  </section>
  <div class="abs notch" style="top:245px;background:var(--white)"></div>

  <section class="abs programs">
    <h2 class="abs sec-title serif" style="top:10px;font-weight:400">Fitness Programs To Fit Your Needs</h2>
    <p class="abs sec-sub" style="top:28px">Take a look at the different fitness classes we offer and check out the one that fits you best.</p>
    <div class="abs card" style="left:15px">
      <div class="ph" role="img" aria-label="Woman training on an elliptical machine" style="background:linear-gradient(135deg,#d9dde0,#8fa3ad)"></div>
      <h3>1 On 1 Personal Training</h3>
      <p>We have over two dozen qualified coaches<br>that are excited to help you meet your fitness goals.<br>See what we have</p>
      <span class="more">Learn more ...</span>
    </div>
    <div class="abs card" style="left:131px">
      <div class="ph ph-label" role="img" aria-label="Athlete lifting a dumbbell" style="background:linear-gradient(135deg,#7a6a60,#3e3835)">Learn more ...</div>
      <h3>Online Strength Coaching</h3>
      <p>See whats going on inside the gym.<br>Check out the Online Strength Coaching</p>
      <span class="more">Learn more ...</span>
    </div>
    <div class="abs card" style="left:247px">
      <div class="ph" role="img" aria-label="Two people on exercise bikes" style="background:linear-gradient(135deg,#e4e4e4,#8a8a8a)"></div>
      <h3>Strength Programming</h3>
      <p>Take a minute to get to know this program<br>and try it</p>
      <span class="more">Learn more ...</span>
    </div>
  </section>
  <div class="abs notch" style="top:436px;background:var(--dark)"></div>

  <section class="abs join" role="img" aria-label="Woman resting after a workout, dark photo">
    <h2 class="abs serif">Join My Programs Now</h2>
    <p class="abs">We don't want you to have to worry about how many classes a week you have on your plan, we want you to come as frequently as you need to in order to achieve the results you're wanting. It doesn't get any easier than that ...</p>
    <div class="abs btn">Get Started Today</div>
  </section>
  <div class="abs notch" style="top:543px;background:var(--white)"></div>

  <section class="abs success">
    <h2 class="abs sec-title serif" style="top:10px;font-weight:400">Success Story</h2>
    <div class="abs person" style="left:12px"><div class="avatar" role="img" aria-label="Portrait photo of client" style="background:#8a6a55"></div><h4>Marco Vance</h4><div class="role">Gym Coach</div><q>"Just give it a shot!<br>What do you have to lose? ".</q></div>
    <div class="abs person" style="left:100px"><div class="avatar" role="img" aria-label="Portrait photo of client" style="background:#6f8a6a"></div><h4>Lena Brooks</h4><div class="role">Aerobic Leader</div><q>"The sense of community<br>that you get from the other members<br>as well as the feedback<br>from the coaches".</q></div>
    <div class="abs person" style="left:188px"><div class="avatar" role="img" aria-label="Portrait photo of client" style="background:#c79a7c"></div><h4>Theo</h4><div class="role">Athlete</div><q>"I learned that<br>I often underestimate<br>what I'm capable of".</q></div>
    <div class="abs person" style="left:276px"><div class="avatar" role="img" aria-label="Portrait photo of client" style="background:#a9c4cf"></div><h4>Clara Hayes</h4><div class="role">Financial Consultant</div><q>"I've learned that I can push<br>myself harder than<br>I ever though possible.".</q></div>
  </section>

  <footer class="abs footer">
    <div class="abs" style="left:12px;top:8px">
      <div class="f-head">Tessa Lorvel Fitness Training</div>
      <div class="f-row"><i></i>512-607-4918</div>
      <div class="f-row"><i></i>info@tessalorvel.com</div>
      <div class="f-row"><i></i>www.TessaLorvel.com</div>
    </div>
    <div class="abs f-divider"></div>
    <div class="abs f-head" style="left:106px;top:8px">Location</div>
    <div class="abs map" role="img" aria-label="Street map of the studio location"></div>
    <div class="abs" style="left:106px;top:47px;line-height:5px">2738 E 19th St #415<br>Austin, TX 78705</div>
    <div class="abs f-head" style="right:10px;top:8px">Connect With Me</div>
    <div class="abs social"><i></i><i></i><i></i><i></i><i></i><i></i></div>
    <div class="abs legal">Blog &nbsp;|&nbsp; Privacy Policy &nbsp;|&nbsp; Terms of Use</div>
  </footer>
  <div class="abs bottom">© 2015, Tessa Lorvel Fitness Training</div>
</div>
</body>
</html>
```